Vortelan d.o.o. needes a web site design

We are a company dealing with automatic doors, industrial doors, roller shutters, access control systems.
We would like to get a design which is clean and neat, and here are some sites which work with similar products. These designs are some we like, but of course, I am looking for a design which is unique. We usually use grey and red colours, which you can see on www.vortelan.ba .
The sites we like are:
http://www.plexawin.com/gb/
http://www.brunosteca.it/eng/
http://faswoodportamel.com/

You have to understand, that we have 4 different groups of products, which are main groups. I would like if those 4 groups somehow could be in different colours. (Maybe "zuvex" colours), in order to separate the groups in some way.

Attached you have web site structure.

If any questions, please contact me.
Edvin

Target Market(s)

Bosnian market. Aluminium and PVC doors and window market, Construction companies, Supermarkets-Retail, Gas stations, Banks, Food industry, Heavy industry.

Industry/Entity Type

It Company

Contact Information for Business Card

I have attached our current business card in PDF. I weould like english on one side, bosnian on other side.

Logo Text

Vortelan is the name of the company, our core business is automation!

Number of Pages Required

5+ page

Font styles to use
Sans Serif

Colors
ec1f27
0792cd
9bcb3c
ffc214
ffffff

```html
<!DOCTYPE html>
<html lang="bs">
<head>
<meta charset="utf-8">
<title>Vortelan d.o.o.</title>
<link href="https://fonts.googleapis.com/css2?family=Oswald:wght@400;500&family=Lato:ital,wght@0,400;0,700;1,400&display=swap" rel="stylesheet">
<style>
:root{
  --red:#d72a3a;
  --brand-red:#ec1f27;
  --blue:#0792cd;
  --green:#9bcb3c;
  --yellow:#ffc214;
  --ink:#3b3b3b;
  --muted:#8a8a8a;
  --band:#ededed;
  --dark:#2c2c2c;
  --white:#ffffff;
}
*{box-sizing:border-box;margin:0;padding:0}
html,body{width:1200px;height:2267px;overflow:hidden;background:var(--white)}
body{position:relative;font-family:'Lato',sans-serif;color:var(--ink)}
.abs{position:absolute}

/* header */
.site-header{left:0;top:0;width:1200px;height:128px;background:var(--white)}
.brand{left:47px;top:12px;width:283px;height:109px;display:flex;align-items:center;gap:14px;padding-left:12px}
.brand-mark{width:26px;height:26px;background:var(--brand-red)}
.brand-name{font-family:'Lato',sans-serif;font-weight:700;font-size:34px;color:var(--ink)}
.cta-redesign{left:881px;top:30px;width:270px;height:70px;background:var(--red);color:var(--white);font-family:'Lato',sans-serif;font-weight:700;font-size:24px;display:flex;align-items:center;justify-content:center}

/* hero */
.hero{left:0;top:128px;width:1200px;height:529px;background:linear-gradient(100deg,#1f4b63 0%,#3d6e86 45%,#5a8aa0 70%,#2e5a70 100%)}
.hero-title{right:49px;top:298px;font-family:'Oswald',sans-serif;font-weight:500;font-size:62px;line-height:1;color:var(--white);text-align:right}
.hero-sub{right:49px;top:386px;font-size:22px;line-height:29px;color:var(--white);text-align:right}
.hero-dots{left:1078px;top:513px;display:flex;gap:8px}
.hero-dots span{width:16px;height:16px;border-radius:50%;border:2px solid #d9e3e8}
.hero-dots span.active{background:var(--brand-red);border-color:var(--brand-red)}

/* welcome */
.welcome-rule{top:722px;height:2px;background:#e4e4e4}
.welcome-title{left:0;width:1200px;top:700px;text-align:center;font-family:'Oswald',sans-serif;font-weight:500;font-size:31px;color:var(--ink)}
.welcome-title em{font-style:normal;color:var(--brand-red)}
.welcome-text{left:106px;top:774px;width:992px;text-align:center;font-size:12px;line-height:21px;color:var(--muted)}
.btn-read{left:527px;top:854px;width:142px;height:44px;background:var(--red);color:var(--white);font-size:12px;display:flex;align-items:center;justify-content:center}

/* product groups */
.group{top:987px;width:261px;height:315px;display:flex;align-items:center;justify-content:center;text-align:center;font-family:'Oswald',sans-serif;font-size:34px;line-height:41px;color:#111}
.group-automatic{left:47px;background:linear-gradient(160deg,#f04a55,#d2232d)}
.group-industrial{left:609px;background:linear-gradient(160deg,#a6d24a,#8fc035)}
.group-access{left:890px;background:linear-gradient(160deg,#ffcc33,#f0b000)}
.group-shutters{left:328px;background:linear-gradient(180deg,#7d7f82 0%,#4b4c4f 55%,#c9cacb 100%)}
.group-more{left:328px;top:1266px;width:261px;height:36px;background:var(--blue);color:var(--white);font-family:'Oswald',sans-serif;font-size:19px;display:flex;align-items:center;justify-content:center;gap:14px}

/* testimonial */
.testimonials{left:0;top:1363px;width:1200px;height:299px;background:var(--band)}
.quote-box{left:364px;top:1413px;width:399px;height:169px;background:var(--white);padding:42px 24px 0 24px;font-style:italic;font-size:12px;line-height:22px;color:#a3a3a3}
.quote-mark{left:356px;top:1388px;font-family:Georgia,serif;font-size:78px;line-height:1;color:#c9c9c9}
.quote-tail{left:763px;top:1452px}
.avatar{left:810px;top:1419px;width:72px;height:72px;border-radius:50%;background:linear-gradient(180deg,#e3c7ae,#33415a);border:3px solid var(--white)}
.author{left:786px;top:1500px;width:120px;text-align:center}
.author-name{font-size:21px;font-weight:700;color:#555}
.author-city{font-size:11px;color:#999;margin-top:2px}

/* get started */
.get-started{left:0;top:1662px;width:1200px;height:526px;background:radial-gradient(ellipse at 40% 55%,#4a4a4a 0%,#2f2f2f 55%,#232323 100%)}
.gs-title{left:76px;top:1754px;font-family:'Oswald',sans-serif;font-weight:400;font-size:31px;color:var(--white)}
.gs-title em{font-style:normal;color:var(--brand-red)}
.gs-text{left:76px;top:1812px;width:490px;font-size:12px;line-height:19px;color:var(--white)}
.gs-rule{left:76px;top:1889px;width:488px;height:1px;background:#cfcfcf}
.contact{left:80px;top:1915px;font-size:15px;line-height:28.7px;color:var(--white);font-style:normal}
.contact .email{margin-top:28px}
.field{left:654px;width:488px;border:1px solid #bdbdbd;background:rgba(255,255,255,0.08);color:var(--white);font-size:15px;padding:6px 14px}
.field-name{top:1813px;height:35px}
.field-email{top:1880px;height:34px}
.field-phone{top:1946px;height:35px}
.field-address{top:2007px;height:86px}
.btn-send{left:1006px;top:2111px;width:135px;height:41px;background:var(--white);color:var(--brand-red);font-size:21px;display:flex;align-items:center;justify-content:center;letter-spacing:1px}

/* footer */
.site-footer{left:0;top:2188px;width:1200px;height:79px;background:var(--red)}
.copyright{left:0;width:1190px;top:2216px;text-align:center;font-size:10px;color:var(--white)}
.social{top:2210px;width:27px;height:27px;border:1px solid var(--white)}
</style>
</head>
<body>

<header class="abs site-header"></header>
<div class="abs brand"><span class="brand-mark"></span><span class="brand-name">vortelan d.o.o.</span></div>
<a class="abs cta-redesign">Redizajn Stranice</a>

<section class="abs hero" role="img" aria-label="Photo of glass automatic sliding doors at a building entrance"></section>
<h1 class="abs hero-title">NOVA WEB STRANICA</h1>
<p class="abs hero-sub">u toku su radovi na novoj web prezentaciji naših usluga,<br>uskoro smo ponovo sa vama</p>
<div class="abs hero-dots"><span class="active"></span><span></span><span></span></div>

<div class="abs welcome-rule" style="left:47px;width:364px"></div>
<div class="abs welcome-rule" style="left:789px;width:362px"></div>
<h2 class="abs welcome-title">WELCOME TO <em>V</em>ORTEL<em>A</em>N</h2>
<p class="abs welcome-text">Lorem ipsum dolor sit amet, consectetur adipiscing elit, sed do eiusmod tempor incididunt ut labore et dolore magna aliqua. Ut enim ad minim veniam, quis nostrud exercitation ullamco laboris nisi ut aliquip ex ea commodo consequat. Duis aute irure dolor in reprehenderit in voluptate velit esse cillum dolore eu fugiat nulla pariatur. Excepteur sint occaecat cupidatat non proident, sunt in culpa qui officia deserunt mollit anim id est laborum.</p>
<a class="abs btn-read">READ MORE</a>

<div class="abs group group-automatic" role="img" aria-label="Automatic doors photo in red tint">Automatic<br>Doors</div>
<div class="abs group group-shutters" role="img" aria-label="Photo of a closed roller shutter"></div>
<a class="abs group-more">READ MORE
  <svg width="24" height="24" viewBox="0 0 24 24"><circle cx="12" cy="12" r="10.5" fill="none" stroke="#fff" stroke-width="2"/><path d="M10 7l5 5-5 5" fill="none" stroke="#fff" stroke-width="2"/></svg>
</a>
<div class="abs group group-industrial" role="img" aria-label="Industrial door photo in green tint">Industrial<br>Doors</div>
<div class="abs group group-access" role="img" aria-label="Access control photo in yellow tint">Access Control<br>Systems</div>

<section class="abs testimonials"></section>
<svg class="abs" style="left:196px;top:1443px" width="40" height="108" viewBox="0 0 40 108"><path d="M38 2L2 54l36 52" fill="none" stroke="#b5b5b5" stroke-width="2"/></svg>
<svg class="abs" style="left:1004px;top:1443px" width="40" height="108" viewBox="0 0 40 108"><path d="M2 2l36 52L2 106" fill="none" stroke="#b5b5b5" stroke-width="2"/></svg>
<blockquote class="abs quote-box">Lorem ipsum dolor sit amet, consectetur adipiscing elit, sed do eiusmod tempor incididunt ut labore et dolore magna aliqua. Ut enim ad minim veniam, quis nostrud exercitation ullamco laboris nisi ut aliquip ex ea commodo consequat.</blockquote>
<span class="abs quote-mark">&ldquo;</span>
<svg class="abs quote-tail" width="22" height="24" viewBox="0 0 22 24"><path d="M0 0L22 0L0 24Z" fill="#fff"/></svg>
<div class="abs avatar" role="img" aria-label="Client portrait"></div>
<div class="abs author"><div class="author-name">Dario Kelm</div><div class="author-city">City&nbsp; Location</div></div>

<section class="abs get-started" role="img" aria-label="Dark photo of a hand touching a tablet screen"></section>
<h2 class="abs gs-title">GET <em>S</em>TARTED</h2>
<p class="abs gs-text">Lorem ipsum dolor sit amet, consectetur adipiscing elit, sed do eiusmod tempor incididunt ut labore et dolore magna aliqua. Ut enim ad minim veniam, quis nostrud exercitation ullamco laboris nisi ut aliquip ex ea commodo consequat.</p>
<div class="abs gs-rule"></div>
<address class="abs contact">
  Ravnih Polja BB,<br>78420 LUKAVAC<br>Telefon: 035/412-560<br>Fax: 035/412-561<br>Mobitel: 061/318-274
  <div class="email">E-mail: info@vortelan.ba</div>
</address>
<div class="abs field field-name">Name</div>
<div class="abs field field-email">Email id</div>
<div class="abs field field-phone">Phone</div>
<div class="abs field field-address">Address</div>
<a class="abs btn-send">SEND</a>

<footer class="abs site-footer"></footer>
<p class="abs copyright">Copyright 2016 Company Name. All Rights Reserved.</p>
<span class="abs social" style="left:1002px"></span>
<span class="abs social" style="left:1041px"></span>
<span class="abs social" style="left:1079px;background:var(--white)"></span>
<span class="abs social" style="left:1118px"></span>

</body>
</html>
```